VelaMarina Passport 4 Page A5 Brochure

DESIGN BRIEF – VelaMarina Passport Brochure
Project Title
VelaMarina Passport – A5 4-Page Brochure Design
________________________________________
Overview
We are looking for a designer to create a clean, visually appealing A5, 4-page brochure to present The VelaMarina Passport to local businesses.
The brochure will be used as a sales and information document and should feel:
• Premium
• Friendly
• Professional
• Easy to understand
• Fun and engaging
The audience is bar owners, venue managers, restaurants, clubs, hotels, and local businesses in Maspalomas.
Format & Technical Requirements
• Size: A5
• Pages: 4 (front cover, 2 inside pages, back cover)
• Orientation: Portrait
• Print-ready design
• Space-aware layouts (some content will be added later)
Brand & Tone
• Brand: VelaMarina
• Location: Maspalomas / Gran Canaria
• Target audience: LGBTQ+ friendly venues and tourism businesses
• Style:
o Modern
o Warm
o Professional
o Island-inspired
o Not overly corporate
• Avoid clutter — white space is welcome
PAGE-BY-PAGE REQUIREMENTS
PAGE 1 – FRONT COVER
Purpose: First impression & visual impact
Requirements:
• Strong visual design
• Clear title: “The VelaMarina Passport”
• Subheading example:
A premium voucher booklet connecting tourists with local venues
• Leave a clear placeholder space for:
o An image of the Passport front cover
• We are open to designers also proposing a design for the Passport front cover itself (optional extra – happy to receive bids for this)
Style notes:
• Eye-catching but elegant
• Feel of travel, discovery, nightlife, and local culture
PAGE 2 – INSIDE LEFT
Purpose: Explain the concept – text provided
Content:
• Short overview of:
o What The VelaMarina Passport is
o Targeted distribution
o Key benefits (high-value visitors, no wasted reach, transferable, no expiry)
• Icons or visual blocks encouraged
• Easy-to-scan layout
Design Notes:
• Use headings, icons, or info blocks
• Avoid large walls of text
PAGE 3 – INSIDE RIGHT (How the Passport Works in Practice)
Purpose:
To visually explain how The VelaMarina Passport is owned, transferred, and used, while showing real examples of how venues appear inside the booklet.
Required Elements
1. Passport Ownership & Transfer Section
The Passport can be owned by up to three people in total (original owner + two transfers).
This page should include three clearly defined visual placeholders representing:
• Original Passport Owner
• Transfer 1 – New Owner
• Transfer 2 – Final Owner
These can be shown as:
• Three mini page mockups
• Three outlined boxes with headings
• Or a creative, passport-style visual layout
Each section should clearly show space for:
• Name
• Country (optional)
• Signature
• Date
👉 We are open to creative proposals for the design of this transfer page and happy to receive bids specifically for designing this page as part of the Passport.
2. Example Voucher Advert Section
This page should also include space to show an example of a voucher advert page, displayed as a mock layout only.
The example should visually communicate:
• Venue name & logo
• Short venue description
• Example offer (e.g. “Free signature shot”)
• Voucher box to be crossed off by staff
This is illustrative only — final content will be provided later.
Design Notes
• Keep the layout clear and easy to understand at a glance
• Visual explanation is more important than text
• Use icons, borders, or soft background panels to separate sections
• The tone should feel official but friendly, similar to a real passport
• Avoid clutter — white space is encouraged
Key Message to Communicate Visually
• The Passport has real ownership
• It can be passed on
• Vouchers are clearly controlled
• Each page feels premium, structured, and easy to use
PAGE 4 – BACK COVER
Purpose: Commercial offer & call to action
Content requirements:
• Clear presentation of two participation options:
1. Voucher Page (incentivised pricing)
2. Standard Advertising Page (no voucher)
• Simple comparison layout encouraged
Visual placeholders required:
• Space to show:
o A sample voucher page
o A sample advert-only page
Contact Details Area:
• VelaMarina logo or name
• Contact text placeholder (phone / email / website)
• Clean, professional call to action
Design Flexibility
We are happy to:
• Receive creative layout suggestions
• See optional icon sets
• See colour palette ideas
• Receive proposals that slightly refine the structure (as long as all elements are included)
Deliverables
• Final A5 4-page brochure design
• Print-ready PDF
• Editable source files (preferred)
• Clear indication of any optional extras (e.g. Passport cover design)
What We’re Looking For
• Clean layout
• Strong hierarchy
• Clear visual storytelling
• Understanding of hospitality / nightlife / tourism
• Ability to balance fun with professionalism
Optional Extras (welcome but not required)
• Proposal for the Passport front cover design
• Proposal for the transfer page design
• Icon set or mini graphic elements
• Alternative colour version
Notes to Designers
This brochure will be used repeatedly and updated over time, so clarity, flexibility, and strong structure are more important than heavy decoration.
We look forward to creative, thoughtful proposals.

Target Market(s)

LGBTIQ+ Tourists and Businesses

Industry/Entity Type

Tourism

Requirements
Must have
• meet the 4 page brief
Nice to have
• proposals for design elements within the design

```html
<!DOCTYPE html>
<html lang="en">
<head>
<meta charset="utf-8">
<title>VelaMarina Passport – A5 Brochure</title>
<link rel="stylesheet" href="https://fonts.googleapis.com/css2?family=Comfortaa:wght@700&family=Lexend:wght@400;500;600;700&display=swap">
<style>
:root{
  --bg:#f4f4f4;
  --blue-deep:#3b55a8;
  --blue-mid:#3f6cc4;
  --blue-sky:#4fb0e4;
  --band:#3a4fa0;
  --cream:#f6efe8;
  --cream-dark:#ece2d6;
  --brown:#5a3e1b;
  --tan:#ddb06e;
  --gold:#d9a45c;
  --ink:#1f160c;
  --white:#ffffff;
  --head:"Comfortaa", sans-serif;
  --body:"Lexend", sans-serif;
}
*{box-sizing:border-box;margin:0;padding:0}
html,body{width:976px;height:1200px;overflow:hidden;background:var(--bg)}
.spread{position:relative;width:976px;height:1200px}
.page{position:absolute;width:410px;height:580px;overflow:hidden;box-shadow:0 6px 18px rgba(0,0,0,.12)}
.p1{left:69px;top:11px}
.p2{left:497px;top:11px}
.p3{left:69px;top:609px}
.p4{left:497px;top:609px}

/* blue pages */
.blue{background:linear-gradient(160deg,var(--blue-sky) 0%,var(--blue-mid) 30%,var(--blue-deep) 60%,var(--blue-mid) 85%,var(--blue-sky) 100%);color:var(--white)}
.island-art{position:absolute;inset:0;background:radial-gradient(ellipse 70% 18% at 50% 12%,rgba(120,160,225,.35),transparent 70%),radial-gradient(ellipse 80% 20% at 45% 70%,rgba(140,160,230,.35),transparent 70%)}
.brand{position:absolute;left:0;right:0;text-align:center;font-family:var(--body)}
.brand-row{display:flex;align-items:center;justify-content:center;gap:8px}
.brand-dot{width:16px;height:16px;border-radius:50%;background:#f2c230}
.brand-name{font-weight:600;letter-spacing:.5px}
.brand-tag{font-family:var(--head);font-size:11px}
.cover-brand{top:62px}
.cover-brand .brand-name{font-size:34px}
.cover-brand .brand-tag{margin-left:60px;margin-top:2px}
.cover-title{position:absolute;top:215px;left:0;right:0;text-align:center;font-family:var(--body);font-weight:500;font-size:45px;line-height:48px;letter-spacing:1px}
.cover-sub{position:absolute;top:464px;left:0;right:0;text-align:center;font-family:var(--body);font-size:14px;line-height:18px}
.cover-band{position:absolute;top:524px;left:0;right:0;height:22px;background:var(--band);text-align:center;font-family:var(--body);font-weight:600;font-size:13px;line-height:22px}

/* cream pages */
.cream{background:linear-gradient(170deg,var(--cream-dark),var(--cream) 40%,var(--cream) 70%,var(--cream-dark));color:var(--ink)}
.heading{position:absolute;left:0;right:0;text-align:center;font-family:var(--head);font-size:19px;color:var(--brown);line-height:24px}
.body-text{position:absolute;left:30px;right:30px;text-align:center;font-family:var(--body);font-size:7.6px;line-height:11px;color:var(--ink)}
.pill{position:absolute;top:171px;left:140px;width:131px;height:21px;border-radius:7px;background:var(--brown);color:var(--white);text-align:center;font-family:var(--head);font-size:12px;line-height:21px}
.benefit{position:absolute;width:160px;text-align:center;font-family:var(--body);font-weight:600;font-size:11px;color:var(--ink)}
.benefit svg{display:block;margin:0 auto 6px}

/* transfer page */
.gold-sub{position:absolute;top:112px;left:0;right:0;text-align:center;font-family:var(--body);font-weight:600;font-size:12.5px;color:var(--gold)}
.owner-note{top:140px;font-size:9.5px;line-height:13px}
.owner{position:absolute;left:24px;width:362px;height:106px}
.owner-frame{position:absolute;left:100px;right:0;top:0;bottom:0;border:1.5px dashed var(--brown);border-left:none;border-radius:0 12px 12px 0}
.owner-tab{position:absolute;left:0;top:0;width:122px;height:106px;border-radius:12px;display:flex;align-items:center;padding-left:14px;gap:8px;color:var(--white);font-family:var(--body);font-weight:500}
.owner-tab.dark{background:var(--brown)}
.owner-tab.light{background:var(--tan)}
.owner-num{font-size:34px;font-weight:500}
.owner-label{font-size:16px;line-height:17px}
.owner-arrow{position:absolute;left:38px;top:-2px}
.fields{position:absolute;left:130px;right:14px;top:14px}
.field{display:flex;align-items:flex-end;height:20.5px;font-family:var(--body);font-weight:500;font-size:7px;color:var(--gold)}
.field .line{flex:1;border-bottom:1px solid var(--gold);margin-left:8px;margin-bottom:2px}
.field small{font-size:3px;margin-left:1px}

/* back cover */
.offer{position:absolute;left:34px;width:342px;height:121px;border:1.5px dashed var(--brown);border-radius:12px;background:var(--cream);padding:10px 20px 0}
.offer-title{text-align:center;font-family:var(--body);font-size:13px;color:var(--brown);margin-bottom:2px}
.offer .field{height:20.5px}
.contact-band{position:absolute;top:460px;left:0;right:0;height:95px;background:var(--band)}
.back-brand{top:24px;left:28px;right:auto;width:160px}
.back-brand .brand-name{font-size:19px}
.back-brand .brand-dot{width:11px;height:11px}
.back-brand .brand-tag{font-size:6px;margin-top:1px}
.contact{position:absolute;left:243px;top:10px;font-family:var(--body);font-weight:600}
.contact-label{font-size:9px}
.contact-phone{font-size:20px;padding-bottom:3px;border-bottom:1.5px solid var(--white);margin-bottom:5px}
.contact-line{font-size:9.5px;line-height:12px}
</style>
</head>
<body>
<main class="spread">

  <!-- Page 1: front cover -->
  <section class="page p1 blue">
    <div class="island-art" role="img" aria-label="Soft island map illustration of Gran Canaria in blue tones"></div>
    <div class="brand cover-brand">
      <div class="brand-row"><span class="brand-dot"></span><span class="brand-name">VelaMarina</span></div>
      <div class="brand-tag">Sun, sea and open doors...</div>
    </div>
    <h1 class="cover-title">THE<br>VELAMARINA<br>PASSPORT</h1>
    <p class="cover-sub">A premium voucher booklet connecting<br>tourists with local venues</p>
    <div class="cover-band">Maspalomas / Gran Canaria</div>
  </section>

  <!-- Page 2: concept -->
  <section class="page p2 cream">
    <div class="island-art" role="img" aria-label="Faint island map illustration in cream tones" style="opacity:.4"></div>
    <h2 class="heading" style="top:63px">What the VelaMarina Passport is</h2>
    <p class="body-text" style="top:96px">Our Social is an excellent way to meet new friends in a social and fun environment. Our VelaMarina Host will be with you throughout the evening, introducing you to those joining the evening and providing you with information and tips on how best to enjoy Gran Canaria. Perfect for solo travellers, couples, or groups of friends.</p>
    <div class="pill">Key Benefits</div>

    <div class="benefit" style="left:45px;top:230px">
      <svg width="48" height="42" viewBox="0 0 48 42"><path d="M12 2h24l10 12L24 40 2 14z" fill="var(--brown)"/><path d="M2 14h44M12 2l6 12 6-12 6 12 6-12M18 14l6 26 6-26" stroke="var(--cream)" stroke-width="1.5" fill="none"/></svg>
      High-value Visitors
    </div>
    <div class="benefit" style="left:205px;top:228px">
      <svg width="48" height="46" viewBox="0 0 48 46"><path d="M6 16h8l16-10v30L14 26H6z" fill="none" stroke="var(--brown)" stroke-width="4" stroke-linejoin="round"/><path d="M10 26l4 12h5l-3-12" fill="var(--brown)"/><circle cx="36" cy="34" r="9" fill="var(--brown)"/><path d="M32 30l8 8M40 30l-8 8" stroke="var(--cream)" stroke-width="2.2"/></svg>
      No Wasted Reach
    </div>
    <div class="benefit" style="left:45px;top:340px">
      <svg width="44" height="44" viewBox="0 0 44 44"><path d="M14 40V8M6 30l8 10 8-10" stroke="var(--brown)" stroke-width="5" fill="none"/><path d="M30 4v32M22 14l8-10 8 10" stroke="var(--brown)" stroke-width="5" fill="none"/></svg>
      Transferable
    </div>
    <div class="benefit" style="left:205px;top:340px">
      <svg width="46" height="46" viewBox="0 0 46 46"><circle cx="23" cy="23" r="21" fill="var(--brown)"/><path d="M23 23c-4-6-12-6-12 0s8 6 12 0 12-6 12 0-8 6-12 0" stroke="var(--cream)" stroke-width="2.5" fill="none"/></svg>
      No Expiry
    </div>

    <h2 class="heading" style="top:445px">Targeted distribution</h2>
    <p class="body-text" style="top:473px;left:30px;right:30px;text-align:justify;text-align-last:center">Lorem ipsum dolor sit amet, consectetuer adipiscing elit, sed diam nonummy nibh euismod tincidunt ut laoreet dolore magna aliquam erat volutpat. Ut wisi enim ad minim veniam, quis nostrud exerci tation ullamcorper suscipit lobortis nisl ut aliquip ex ea commodo consequat. Duis autem vel eum iriure dolor in hendrerit in vulputate velit esse molestie consequa.</p>
  </section>

  <!-- Page 3: ownership and transfer -->
  <section class="page p3 cream">
    <div class="island-art" role="img" aria-label="Faint island map illustration in cream tones" style="opacity:.4"></div>
    <h2 class="heading" style="top:41px;font-size:21px;line-height:24px">How the Passport<br>Works in Practice</h2>
    <div class="gold-sub">Passport Ownership &amp; Transfer Section</div>
    <p class="body-text owner-note">The Passport can be owned by up to three people in total<br>(original owner + two transfers).</p>

    <div class="owner" style="top:186px">
      <div class="owner-frame"></div>
      <div class="owner-tab dark"><span class="owner-num">1</span><span class="owner-label">Original<br>Owner</span></div>
      <div class="fields">
        <div class="field">Name<span class="line"></span></div>
        <div class="field">Country<small>(opt.)</small><span class="line"></span></div>
        <div class="field">Signature<span class="line"></span></div>
        <div class="field">Date<span class="line"></span></div>
      </div>
    </div>

    <div class="owner" style="top:310px">
      <div class="owner-frame"></div>
      <div class="owner-tab light"><span class="owner-num">2</span><span class="owner-label">New<br>Owner</span></div>
      <svg class="owner-arrow" width="42" height="32" viewBox="0 0 42 32"><path d="M13 0h16v14h11L21 32 2 14h11z" fill="var(--white)"/></svg>
      <div class="fields">
        <div class="field">Name<span class="line"></span></div>
        <div class="field">Country<small>(opt.)</small><span class="line"></span></div>
        <div class="field">Signature<span class="line"></span></div>
        <div class="field">Date<span class="line"></span></div>
      </div>
    </div>

    <div class="owner" style="top:434px">
      <div class="owner-frame"></div>
      <div class="owner-tab dark"><span class="owner-num">3</span><span class="owner-label">Final<br>Owner</span></div>
      <svg class="owner-arrow" width="42" height="32" viewBox="0 0 42 32"><path d="M13 0h16v14h11L21 32 2 14h11z" fill="var(--white)"/></svg>
      <div class="fields">
        <div class="field">Name<span class="line"></span></div>
        <div class="field">Country<small>(opt.)</small><span class="line"></span></div>
        <div class="field">Signature<span class="line"></span></div>
        <div class="field">Date<span class="line"></span></div>
      </div>
    </div>
  </section>

  <!-- Page 4: back cover -->
  <section class="page p4 blue">
    <div class="island-art" role="img" aria-label="Soft island map illustration of Gran Canaria in blue tones"></div>
    <div class="offer" style="top:134px">
      <div class="offer-title">Voucher Page</div>
      <div class="field">Name<span class="line"></span></div>
      <div class="field">Country<small>(opt.)</small><span class="line"></span></div>
      <div class="field">Signature<span class="line"></span></div>
      <div class="field">Date<span class="line"></span></div>
    </div>
    <div class="offer" style="top:271px">
      <div class="offer-title">Standard Advertising Page</div>
      <div class="field">Name<span class="line"></span></div>
      <div class="field">Country<small>(opt.)</small><span class="line"></span></div>
      <div class="field">Signature<span class="line"></span></div>
      <div class="field">Date<span class="line"></span></div>
    </div>
    <div class="contact-band">
      <div class="brand back-brand">
        <div class="brand-row"><span class="brand-dot"></span><span class="brand-name">VelaMarina</span></div>
        <div class="brand-tag">Sun, sea and open doors...</div>
      </div>
      <div class="contact">
        <div class="contact-label">Contact us:</div>
        <div class="contact-phone">555-010-246</div>
        <div class="contact-line">hello@velamarina.example</div>
        <div class="contact-line">www.velamarina.example</div>
      </div>
    </div>
  </section>

</main>
</body>
</html>
```